Family owned plumbing contractor needs eye catching business card design

Business cards that are unique, eye catching, and provide customers with general company information, such as name, address, phone number, website, employee name/title, cell phone #, & email address. We are transitioning to a new logo that utilizes a more retro feel, so we are interested in seeing some cool old school designs in the mix. We are liking the dark background on some of the samples on this website. If that is workable with our artwork, we would like to see that incorporated into the design.
Contact Information for Business Card
Copperline Pipeworks, Inc.
www.copperlinepipeworks.example
(555) 392-7068 phone
Nevada License #64205
California License #5810473
Dale Wrennick, President
(555) 618-9032 cell
dale@copperlinepipeworks.example
Residential * Commercial * Service
Requirements
Must have
- The business card details listed above & logo provided.
Nice to have
- I made some notes about color options in the description.

```html
<!DOCTYPE html>
<html lang="en">
<head>
<meta charset="utf-8">
<title>Copperline Pipeworks – Business Card</title>
<link href="https://fonts.googleapis.com/css2?family=Noto+Sans:wght@400;600;700&display=swap" rel="stylesheet">
<style>
  :root{
    --backdrop:#8a8a8a;
    --paper:#ffffff;
    --frame:#3e5a6e;
    --ink:#2b2b2b;
    --ink-body:#151515;
    --slate:#5a7f99;
    --teal-light:#a1d0cd;
    --teal:#7cc7bb;
    --steel:#587f98;
    --graphite:#6d6869;
  }
  *{margin:0;padding:0;box-sizing:border-box}
  html,body{width:1200px;height:1200px;overflow:hidden}
  body{background:var(--backdrop);font-family:"Noto Sans",Verdana,sans-serif;position:relative}
  .card{position:absolute;width:840px;height:480px;background:var(--paper);box-shadow:0 6px 18px rgba(0,0,0,.35);overflow:hidden}
  .card-front{left:181px;top:66px}
  .card-back{left:178px;top:618px}

  .front-frame{position:absolute;left:11px;top:12px;width:818px;height:452px;border:3px solid var(--frame);border-radius:6px;overflow:hidden}
  .front-art{position:absolute;left:0;right:0;bottom:0;height:210px;
             background:linear-gradient(180deg,#ffffff 0%,#dcdcdc 18%,#8e8b8c 34%,#a1d0cd 52%,#6f9bab 78%,#587f98 100%)}

  .brand{position:absolute;left:138px;top:92px;height:100px;display:flex;align-items:center;gap:18px}
  .brand-dot{width:100px;height:100px;border-radius:50%;background:var(--slate)}
  .brand-name{font-size:35px;font-weight:700;color:var(--ink);letter-spacing:.8px;white-space:nowrap}

  .back-art{position:absolute;left:540px;top:0;width:300px;height:480px;
            background:linear-gradient(180deg,var(--teal) 0%,#6aa8a7 45%,var(--steel) 100%)}
  .seal{position:absolute;left:595px;top:139px;width:190px;height:190px;border-radius:50%;background:rgba(40,70,90,.09);
        display:flex;align-items:center;justify-content:center;text-align:center;
        font-size:22px;font-weight:700;color:rgba(40,70,90,.2);line-height:28px}

  .contact{position:absolute;left:0;top:0;width:520px;height:480px;color:var(--ink-body)}
  .person{position:absolute;left:53px;top:36px;border-left:3px solid var(--ink-body);padding-left:10px}
  .person-name{font-size:29px;font-weight:600;color:var(--slate);line-height:34px;letter-spacing:.5px}
  .person-title{font-size:17px;font-weight:600;color:var(--slate);line-height:22px;letter-spacing:.8px;margin-top:1px}
  .icon{position:absolute;left:52px}
  .line{position:absolute;left:106px;white-space:nowrap;letter-spacing:1px}
  .phone{font-size:19px;font-weight:600;letter-spacing:1.6px}
  .small{font-size:16.5px;font-weight:600}
  .tagline{position:absolute;left:64px;top:394px;font-size:18px;font-weight:600;letter-spacing:1px;white-space:nowrap}
</style>
</head>
<body>

<section class="card card-front" aria-label="Card front">
  <div class="front-frame">
    <div class="front-art" role="img" aria-label="Decorative grey and teal wave artwork"></div>
  </div>
  <div class="brand">
    <span class="brand-dot"></span>
    <span class="brand-name">Copperline Pipeworks</span>
  </div>
</section>

<section class="card card-back" aria-label="Card back">
  <div class="back-art" role="img" aria-label="Decorative teal curved band artwork"></div>
  <div class="seal">Copperline<br>Pipeworks</div>

  <div class="contact">
    <div class="person">
      <div class="person-name">Dale Wrennick</div>
      <div class="person-title">President</div>
    </div>

    <svg class="icon" style="top:143px" width="36" height="36" viewBox="0 0 36 36" aria-hidden="true">
      <rect width="36" height="36" rx="4" fill="var(--slate)"/>
      <path d="M10,7 L14,7 L16,13 L13,15 C14.5,19 17,21.5 21,23 L23,20 L29,22 L29,26 C29,28 27,29 25,29 C16,28 8,20 7,11 C7,9 8,7 10,7 Z" fill="#fff"/>
    </svg>
    <div class="line phone" style="top:135px">(555) 392-7068</div>
    <div class="line phone" style="top:169px">(555) 618-9032</div>

    <svg class="icon" style="top:215px" width="36" height="27" viewBox="0 0 36 27" aria-hidden="true">
      <rect x="1" y="1" width="34" height="25" rx="1" fill="none" stroke="var(--slate)" stroke-width="2"/>
      <path d="M1,1 L18,15 L35,1 M1,26 L14,12 M35,26 L22,12" fill="none" stroke="var(--slate)" stroke-width="2"/>
    </svg>
    <div class="line small" style="top:216px">dale@copperlinepipeworks.example</div>

    <svg class="icon" style="top:270px" width="36" height="36" viewBox="0 0 36 36" aria-hidden="true">
      <rect width="36" height="36" rx="6" fill="var(--slate)"/>
      <g fill="none" stroke="#fff" stroke-width="1.6">
        <circle cx="18" cy="18" r="11"/><ellipse cx="18" cy="18" rx="5" ry="11"/>
        <path d="M7,18 H29 M9,12 H27 M9,24 H27 M18,7 V29"/>
      </g>
    </svg>
    <div class="line small" style="top:272px">www.copperlinepipeworks.example</div>

    <div class="line small" style="top:318px">Nevada License #64205</div>
    <div class="line small" style="top:349px">California License #5810473</div>

    <div class="tagline">Residential &nbsp;*&nbsp; Commercial &nbsp;*&nbsp; Service</div>
  </div>
</section>

</body>
</html>
```